Copperleaf Motorized Shade Business Card

Hello, we've had our logo made. Now we are looking for a clean and cool looking business card. One side can just be the logo with any design elements that might look good with it. The other side will be Name, Phone Number and Email. There will not be an address on the card.

```html
<!DOCTYPE html>
<html lang="en">
<head>
<meta charset="utf-8">
<title>Copperleaf Motorized Shade – Business Card</title>
<link rel="stylesheet" href="https://fonts.googleapis.com/css2?family=Raleway:wght@400;500&family=Roboto:wght@400;700&display=swap">
<style>
  :root {
    --navy: #0a3595;
    --cyan: #00ffff;
    --icon-cyan: #00d8ff;
    --divider: #485958;
    --ink: #1a1a1a;
    --paper: #ffffff;
    --shadow: #c8c8c8;
  }
  * { margin: 0; padding: 0; box-sizing: border-box; }
  html, body { width: 1200px; height: 348px; overflow: hidden; background: var(--paper); }
  .sheet { position: relative; width: 1200px; height: 348px; }
  .backdrop { position: absolute; inset: 0; }
  .brand-name {
    position: absolute;
    font-family: "Roboto", sans-serif;
    font-weight: 700;
    color: var(--navy);
    text-transform: uppercase;
    line-height: 1.1;
    letter-spacing: 0.04em;
  }
  .front-brand { left: 0; width: 578px; top: 118px; font-size: 30px; text-align: center; }
  .back-brand { right: 61px; top: 82px; font-size: 17px; text-align: right; }
  .holder { position: absolute; left: 669px; top: 72px; font-family: "Raleway", sans-serif; }
  .holder-name { font-size: 20.5px; font-weight: 500; color: var(--ink); line-height: 1.2; }
  .holder-role { font-size: 13.5px; font-weight: 400; color: var(--ink); line-height: 1.1; }
  .rule { position: absolute; height: 3px; background: var(--cyan); }
  .rule-long { left: 669px; top: 111px; width: 174px; }
  .rule-short { left: 669px; top: 117px; width: 69px; }
  .contact {
    position: absolute; right: 61px; display: flex; align-items: center; gap: 12px;
    font-family: "Roboto", sans-serif; font-size: 13px; color: var(--ink);
  }
  .contact-phone { top: 187px; }
  .contact-email { top: 228px; }
  .contact-icon { width: 31px; height: 31px; display: block; }
</style>
</head>
<body>
<div class="sheet">
  <svg class="backdrop" width="1200" height="348" viewBox="0 0 1200 348" aria-hidden="true">
    <!-- front side bands -->
    <rect x="0" y="301" width="578" height="47" fill="var(--navy)"/>
    <polygon points="341,283 349,283 305,327 297,327" fill="var(--shadow)"/>
    <polygon points="0,283 341,283 297,327 0,327" fill="var(--cyan)"/>
    <polygon points="578,207 578,348 426,348" fill="var(--cyan)"/>
    <!-- divider -->
    <rect x="578" y="0" width="44" height="348" fill="var(--divider)"/>
    <!-- back side bands -->
    <rect x="622" y="301" width="578" height="47" fill="var(--navy)"/>
    <polygon points="851,283 859,283 901,327 893,327" fill="var(--shadow)"/>
    <polygon points="859,283 1200,283 1200,327 901,327" fill="var(--cyan)"/>
    <polygon points="622,207 622,348 772,348" fill="var(--cyan)"/>
  </svg>

  <div class="brand-name front-brand">Copperleaf<br>Motorized Shade</div>

  <div class="holder">
    <div class="holder-name">YOUR NAME HERE</div>
    <div class="holder-role">Designation</div>
  </div>
  <div class="rule rule-long"></div>
  <div class="rule rule-short"></div>

  <div class="brand-name back-brand">Copperleaf<br>Motorized Shade</div>

  <div class="contact contact-phone">
    <span>Phone Number Here</span>
    <svg class="contact-icon" viewBox="0 0 31 31" aria-hidden="true">
      <rect width="31" height="31" fill="var(--icon-cyan)"/>
      <polygon points="0,0 31,31 0,31" fill="var(--cyan)"/>
      <rect x="10" y="5" width="11" height="20" rx="1.5" fill="none" stroke="#fff" stroke-width="1.5"/>
      <line x1="10" y1="21" x2="21" y2="21" stroke="#fff" stroke-width="1.2"/>
      <circle cx="15.5" cy="23" r="0.9" fill="#fff"/>
    </svg>
  </div>
  <div class="contact contact-email">
    <span>Email address Here</span>
    <svg class="contact-icon" viewBox="0 0 31 31" aria-hidden="true">
      <rect width="31" height="31" fill="var(--icon-cyan)"/>
      <polygon points="0,0 31,31 0,31" fill="var(--cyan)"/>
      <rect x="6" y="9" width="19" height="13" fill="none" stroke="#fff" stroke-width="1.5"/>
      <polyline points="6,9 15.5,17 25,9" fill="none" stroke="#fff" stroke-width="1.5"/>
      <line x1="6" y1="22" x2="13" y2="15.5" stroke="#fff" stroke-width="1.2"/>
      <line x1="25" y1="22" x2="18" y2="15.5" stroke="#fff" stroke-width="1.2"/>
    </svg>
  </div>
</div>
</body>
</html>
```